Private Chef booking platform landing page design

I need an amazing design for a landing page for my upcoming private chef booking platform Platerva. You can view my current page here: www.platerva.co.uk/mainindex.php. The design on this page is wrong right now. This platform is in Beta and the main purpose is to sign up chefs. Similar to what Rydexa.com is doing with their website -> become a driver. In my case we should have a button that says "become a chef", state the benefits of becoming a chef such as earning extra money, managing your time and bookings, increasing your client base and be creative with your food menus at the same time. Also, somewhere on the website it needs to say that we are currently in Beta mode and sign up to help us grow. In terms of visuals, I want the design to be sleek and clean and also adaptable to mobile devices as I am using html5. You can also re-design the current logo and choose any colours you think would be suitable for such a concept. Similar concept websites: hobwanderly.com and stovlin.com
Updates

Target Market(s)

upper middle class

Industry/Entity Type

Chef

Number of Pages Required

1 page

Font styles to use
Sans Serif

Requirements
Must have
• see brief and check hobwanderly.com and stovlin.com for inspiration and also rydexa.com
Nice to have
• see brief
Should not have
• bad visuals

```html
<!DOCTYPE html>
<html lang="en">
<head>
<meta charset="utf-8">
<title>Platerva — Private Chefs at Home</title>
<link rel="stylesheet" href="https://fonts.googleapis.com/css2?family=Oswald:wght@300;400&family=Montserrat:wght@500;600&family=Playfair+Display:ital@1&display=swap">
<style>
  :root {
    --yellow: #f6c400;
    --black: #000000;
    --white: #ffffff;
    --wood-dark: #2b1a12;
    --wood-mid: #5a3a26;
    --wood-light: #8a5d3b;
  }
  * { box-sizing: border-box; margin: 0; padding: 0; }
  html, body { width: 1200px; height: 1000px; overflow: hidden; background: var(--white); }
  body { position: relative; font-family: "Montserrat", sans-serif; }

  .site-header { position: absolute; left: 0; top: 0; width: 1200px; height: 97px; background: var(--black); }
  .brand { position: absolute; left: 14px; top: 13px; width: 147px; height: 73px; border: 2px solid var(--white);
    display: flex; align-items: center; justify-content: center; gap: 8px;
    color: var(--yellow); font: 600 22px "Montserrat", sans-serif; }
  .brand-dot { width: 12px; height: 12px; border-radius: 50%; background: var(--yellow); }
  .beta-tag { position: absolute; left: 163px; top: 12px; color: var(--white); font: 600 10px "Montserrat", sans-serif; }
  .main-nav { position: absolute; left: 209px; top: 42px; display: flex; align-items: center; height: 24px; }
  .main-nav .marker { width: 6px; height: 24px; background: var(--yellow); margin-right: 8px; }
  .main-nav a { color: var(--white); text-decoration: none; font: 600 12px "Montserrat", sans-serif; margin-right: 21px; }
  .main-nav a.active { color: var(--yellow); }
  .account-links { position: absolute; right: 29px; top: 46px; color: var(--white); font: 600 12px "Montserrat", sans-serif; word-spacing: 3px; }

  .hero { position: absolute; left: 0; top: 97px; width: 1200px; height: 654px;
    background: radial-gradient(ellipse at 50% 45%, var(--wood-light) 0%, var(--wood-mid) 45%, var(--wood-dark) 100%); }
  .hero-title { position: absolute; left: 0; top: 230px; width: 1200px; text-align: center;
    color: var(--yellow); font: 300 58px "Oswald", sans-serif; letter-spacing: 0.5px; }
  .cta-chef { position: absolute; left: 434px; top: 356px; width: 328px; height: 78px; border: 2px solid var(--yellow);
    text-align: center; padding-top: 12px; }
  .cta-chef .cta-label { color: var(--yellow); font: 500 21px "Montserrat", sans-serif; }
  .cta-chef .cta-sub { display: flex; align-items: center; justify-content: center; gap: 6px; margin-top: 1px;
    color: var(--white); font: italic 16px "Playfair Display", serif; }
  .cta-sub .rule { width: 28px; height: 1px; background: var(--white); }
  .btn { position: absolute; top: 486px; width: 170px; height: 47px; font: 400 27px "Oswald", sans-serif;
    display: flex; align-items: center; justify-content: center; }
  .btn-outline { left: 424px; border: 2px solid var(--yellow); color: var(--yellow); }
  .btn-solid { left: 605px; background: var(--yellow); color: var(--black); }
  .double-rule { position: absolute; top: 508px; height: 6px; border-top: 1px solid var(--yellow); border-bottom: 1px solid var(--yellow); }

  .steps { position: absolute; top: 553px; left: 0; width: 1200px; }
  .step { position: absolute; display: flex; align-items: center; gap: 12px;
    color: var(--yellow); font: 600 12px/1.15 "Montserrat", sans-serif; }
  .step-icon { width: 30px; height: 54px; background: var(--yellow); border-radius: 4px; opacity: 0.9; }
  .know-more { position: absolute; left: 558px; top: 568px; color: var(--white); font: italic 18px "Playfair Display", serif; }
  .know-more-arrow { position: absolute; left: 590px; top: 597px; }

  .food-left { position: absolute; left: 0; top: 815px; width: 210px; height: 185px; border-top-right-radius: 160px;
    background: radial-gradient(circle at 30% 60%, #c9553a 0%, #7a4a2e 50%, #3d2a1f 100%); }
  .food-right { position: absolute; left: 1020px; top: 751px; width: 180px; height: 249px; border-bottom-left-radius: 120px;
    background: radial-gradient(circle at 60% 30%, #5b3a2a 0%, #a0352a 55%, #e9ddd0 100%); }

  .section-title { position: absolute; left: 0; top: 885px; width: 1200px; display: flex; justify-content: center; align-items: center; gap: 12px;
    color: var(--yellow); font: 400 36px "Oswald", sans-serif; }
  .section-title .double-rule-inline { width: 38px; height: 6px; border-top: 1px solid var(--yellow); border-bottom: 1px solid var(--yellow); }
  .section-divider { position: absolute; left: 593px; top: 965px; width: 2px; height: 35px; background: var(--yellow); }
</style>
</head>
<body>
  <header class="site-header">
    <div class="brand">Platerva<span class="brand-dot"></span></div>
    <span class="beta-tag">BETA</span>
    <nav class="main-nav">
      <span class="marker"></span>
      <a class="active" href="#">HOME</a>
      <a href="#">BENEFITS</a>
      <a href="#">HOW IT WORKS</a>
      <a href="#">CONTACT</a>
    </nav>
    <div class="account-links">SIGN UP / SIGN IN</div>
  </header>

  <section class="hero" role="img" aria-label="Overhead photo of a wooden kitchen table with a chopping board, mortar, spices, herbs, lemon, pan and knives">
    <h1 class="hero-title">CHEFS MADE MEALS IN YOUR HOME</h1>
    <div class="cta-chef">
      <div class="cta-label">BECOME A PRIVATE CHEF</div>
      <div class="cta-sub"><span class="rule"></span>Earn extra money as a private chef.<span class="rule"></span></div>
    </div>
    <div class="double-rule" style="left:176px; width:208px;"></div>
    <div class="btn btn-outline">BENEFITS</div>
    <div class="btn btn-solid">HOW IT WORKS</div>
    <div class="double-rule" style="left:818px; width:190px;"></div>

    <div class="steps">
      <div class="step" style="left:178px;">BOOK A CHEF<span class="step-icon" role="img" aria-label="Chef figure icon"></span></div>
      <div class="step" style="left:361px; text-align:center;">CHEF TAKE CARE<br>OF EVERYTHING<span class="step-icon" role="img" aria-label="Chef cooking icon" style="width:36px;"></span></div>
      <div class="step" style="left:697px;"><span class="step-icon" role="img" aria-label="Waiter serving icon" style="width:22px;"></span>CHEF COOK FOR YOU<br>AND YOUR GUESTS</div>
      <div class="step" style="left:902px;"><span class="step-icon" role="img" aria-label="Guests dining icon" style="width:66px;"></span>YOU JUST ENJOY<br>THE PARTY</div>
    </div>
    <div class="know-more">know more</div>
    <svg class="know-more-arrow" width="20" height="12" viewBox="0 0 20 12"><polyline points="2,2 10,10 18,2" fill="none" stroke="#f6c400" stroke-width="2.5"/></svg>
  </section>

  <div class="food-left" role="img" aria-label="Bowl of roasted vegetables"></div>
  <div class="food-right" role="img" aria-label="Bowl of peppercorns with garlic and cherry tomatoes"></div>

  <h2 class="section-title"><span class="double-rule-inline"></span>BENEFITS<span class="double-rule-inline"></span></h2>
  <div class="section-divider"></div>
</body>
</html>
```